Billboard design for a small town Oral Surgeon

We are getting several billboards and need a design that highlights the doctors photo, and bullet points of what he does. Our business name is extremely long, so it’s a challenge to figure out how to do this. Maybe just use our logo? Open to ideas.
The logo can be shortened as designer sees fit, meaning we can drop the tag line. Important info to include:
Doctors name is Lorvik Tamsen
The highlighted bullet points are:
•Implants
•wisdom teeth
•Jaw Surgery
•facial trauma
The goal of this billboard is to let our community know that they have an option here in Ada, our town. Many still drive to the city a couple hours away not knowing they now have an option here at home. Having a hard time finding examples of what I have in mind, so hoping this will get us going. I want it as “non-busy” as possible, so no unnecessary lines or anything that competes with the information we are trying to get across.

Target Market(s)

Everyone in town, just trying to spread the word that we are here

Industry/Entity Type

Medical/surgical (oral surgery)

Font styles to use
Sans Serif

Colors
0094D4
00A9DD
6FCCEA
C7EBF8
E9F6FB

Requirements
Must have
• *New note** Due to location of billboard, I prefer the photo of doctor to be on the left side. Must look neat and professional. Must highlight what we do.
Nice to have
• Our colors are a blue-green with silver, against black or white, but I’m flexible on this, I don’t necessarily need the colors highlighted. I’m also flexible on font style, just needs to be easy to read.
Should not have
• Distracting graphics, should not look like a dental office. That’s an issue we have is people thinking we are another dental office, we do not do any general dentistry, it’s surgery only.

```html
<!DOCTYPE html>
<html lang="en">
<head>
<meta charset="utf-8">
<title>Billboard – Ridgeline Valley Oral &amp; Maxillofacial Surgery</title>
<link rel="stylesheet" href="https://fonts.googleapis.com/css2?family=Montserrat:wght@300;400;500;600;700&family=Oswald:wght@600&display=swap">
<style>
  :root {
    --teal: #0089a6;
    --silver: #939598;
    --silver-dark: #76787b;
    --white: #ffffff;
    --ink: #2b2b2b;
    --backdrop: #d4d5d7;
  }
  html, body {
    margin: 0;
    padding: 0;
    width: 1137px;
    height: 1200px;
    overflow: hidden;
    background: var(--backdrop);
  }
  .canvas {
    position: relative;
    width: 1137px;
    height: 1200px;
  }
  .billboard {
    position: absolute;
    left: 30px;
    top: 384px;
    width: 1077px;
    height: 431px;
    box-shadow: 14px 18px 26px rgba(0,0,0,0.35);
  }
  .billboard svg { display: block; }
  .sans { font-family: 'Montserrat', sans-serif; }
  .condensed { font-family: 'Oswald', sans-serif; }
</style>
</head>
<body>
<div class="canvas">
  <div class="billboard">
    <svg width="1077" height="431" viewBox="0 0 1077 431" xmlns="http://www.w3.org/2000/svg">
      <defs>
        <linearGradient id="portrait-tone" x1="0" y1="0" x2="0" y2="1">
          <stop offset="0" stop-color="#e9ddd2"/>
          <stop offset="0.5" stop-color="#c9a48f"/>
          <stop offset="0.72" stop-color="#2a3340"/>
          <stop offset="1" stop-color="#1c2430"/>
        </linearGradient>
      </defs>

      <!-- white header field -->
      <rect class="header-field" x="0" y="0" width="1077" height="216" fill="var(--white)"/>
      <!-- teal band -->
      <rect class="service-band" x="0" y="216" width="1077" height="215" fill="var(--teal)"/>

      <!-- doctor portrait area: narrow at head height, wider at shoulders -->
      <path class="doctor-portrait" role="img" aria-label="Portrait photo of Dr Lorvik Tamsen in a dark suit, white shirt and red tie"
            d="M0 16 H222 V216 H308 V431 H0 Z" fill="url(#portrait-tone)"/>

      <!-- doctor name plate -->
      <rect class="name-plate" x="0" y="341" width="280" height="61" fill="var(--teal)"/>
      <text class="sans name-plate-text" x="140" y="381" text-anchor="middle" font-size="27" font-weight="600" fill="var(--white)">Dr Lorvik Tamsen</text>

      <!-- practice name block -->
      <circle class="practice-mark" cx="340" cy="70" r="40" fill="none" stroke="var(--silver)" stroke-width="4"/>
      <text class="sans practice-name" font-size="15" font-weight="400" fill="var(--ink)">
        <tspan x="238" y="144" textLength="197" lengthAdjust="spacingAndGlyphs">RIDGELINE VALLEY ORAL</tspan>
        <tspan x="238" y="161" textLength="197" lengthAdjust="spacingAndGlyphs">&amp; MAXILLOFACIAL SURGERY</tspan>
      </text>
      <line class="practice-rule" x1="238" y1="167" x2="435" y2="167" stroke="var(--ink)" stroke-width="0.8"/>
      <text class="sans practice-tagline" x="238" y="178" font-size="7.5" font-weight="400" fill="var(--ink)" textLength="197" lengthAdjust="spacing">COMFORT | CARE | COMPASSION</text>

      <!-- headline -->
      <text class="sans headline-top" x="475" y="102" font-size="73" font-weight="600" fill="var(--silver)" textLength="487" lengthAdjust="spacingAndGlyphs">YOUR LOCAL</text>
      <text class="condensed headline-sub" x="475" y="153" font-size="56" font-weight="600" fill="var(--teal)" textLength="487" lengthAdjust="spacingAndGlyphs">ORAL &amp; MAXILLOFACIAL SURGEON</text>

      <!-- ribbon -->
      <path class="ribbon-ear" d="M468 216 L468 207 Q468 198 478 198 L490 198 L490 216 Z" fill="var(--silver-dark)"/>
      <path class="ribbon-ear" d="M899 216 L899 207 Q899 198 889 198 L878 198 L878 216 Z" fill="var(--silver-dark)"/>
      <path class="ribbon" d="M490 198 L878 198 L878 233 Q878 249 862 249 L506 249 Q490 249 490 233 Z" fill="var(--silver)"/>
      <text class="sans ribbon-text" x="684" y="234" text-anchor="middle" font-size="27" font-weight="700" fill="var(--white)">SPECIALIZE IN</text>

      <!-- services -->
      <g class="service-ticks" fill="none" stroke="var(--white)" stroke-width="1.8" stroke-linecap="round" stroke-linejoin="round">
        <g transform="translate(371 312)"><path d="M6 -5.5 A7 7 0 1 0 7 2"/><path d="M-3 0 L0 3 L7 -5"/></g>
        <g transform="translate(371 353)"><path d="M6 -5.5 A7 7 0 1 0 7 2"/><path d="M-3 0 L0 3 L7 -5"/></g>
        <g transform="translate(723 312)"><path d="M6 -5.5 A7 7 0 1 0 7 2"/><path d="M-3 0 L0 3 L7 -5"/></g>
        <g transform="translate(723 353)"><path d="M6 -5.5 A7 7 0 1 0 7 2"/><path d="M-3 0 L0 3 L7 -5"/></g>
      </g>
      <g class="sans service-list" font-size="31" font-weight="500" fill="var(--white)">
        <text x="402" y="324" textLength="159" lengthAdjust="spacingAndGlyphs">IMPLANTS</text>
        <text x="402" y="365" textLength="246" lengthAdjust="spacingAndGlyphs">WISDOM TEETH</text>
        <text x="759" y="324" textLength="228" lengthAdjust="spacingAndGlyphs">JAW SURGERY</text>
        <text x="760" y="365" textLength="255" lengthAdjust="spacingAndGlyphs">FACIAL TRAUMA</text>
      </g>
    </svg>
  </div>
</div>
</body>
</html>
```